Contemporary restaurant add that stands out

I would like an ad that I can use for flyers and in guide books for a tourist restaurant. It must reflect high quality, be contemporary and stand out amongst other adverts.

The ad must try and say good quality food in pleasant surroundings.

The ad must be left open because different guide books require different size ads, so it must be able to resize.

I have included our current ad. I want it changed because some feedback I received say it looks more like a nightclub than a restaurant.

I also have more pics if necessary. Also I have pics of the restaurant in different colours

Target Market(s)

Tourists of various nationalities

Industry/Entity Type

Restaurant

Requirements
Must have
• The name of the restaurant is
• Paper Kite
• And it is in Edwardian script font with bold and italic selected.
• The ad must contain our phone number, address and free wifi. The details are on our current ad which is included

```html
<!DOCTYPE html>
<html lang="en">
<head>
<meta charset="utf-8">
<title>Paper Kite Restaurant Flyer</title>
<link href="https://fonts.googleapis.com/css2?family=Great+Vibes&family=Open+Sans:ital,wght@0,400;0,600;0,700;1,600&display=swap" rel="stylesheet">
<style>
  :root {
    --magenta: #d81e7c;
    --magenta-deep: #b0155f;
    --teal: #2ec4c0;
    --teal-deep: #1a9e9c;
    --white: #ffffff;
    --ink: #333333;
    --night: #120a14;
    --glow: #7a2a8a;
  }
  * { margin: 0; padding: 0; box-sizing: border-box; }
  html, body { width: 870px; height: 1200px; overflow: hidden; background: var(--white); }
  .flyer {
    position: relative; width: 870px; height: 1200px; overflow: hidden;
    background: var(--white); font-family: "Open Sans", Arial, sans-serif; color: var(--ink);
  }
  .backdrop { position: absolute; inset: 0; }

  .venue-photo {
    position: absolute; left: 0; top: 190px; width: 870px; height: 540px;
    background:
      radial-gradient(ellipse at 50% 25%, rgba(190,70,210,0.75) 0%, rgba(120,40,150,0.4) 30%, transparent 60%),
      radial-gradient(ellipse at 50% 75%, rgba(230,120,200,0.35) 0%, transparent 55%),
      linear-gradient(180deg, var(--night) 0%, #2a1030 45%, #3b1840 70%, var(--night) 100%);
  }

  .reservation { position: absolute; left: 52px; top: 62px; color: var(--white); }
  .reservation-label { font-size: 20px; font-weight: 600; }
  .reservation-phone { font-size: 42px; font-weight: 700; letter-spacing: 1px; line-height: 1.2; }

  .brand { position: absolute; right: 40px; top: 22px; text-align: right; }
  .brand-name {
    font-family: "Great Vibes", cursive; font-size: 108px; line-height: 1;
    color: var(--white); display: block;
  }
  .brand-sub { font-size: 30px; font-weight: 600; color: var(--teal); margin-top: -6px; margin-right: 6px; display: block; }

  .dish {
    position: absolute; border-radius: 50%; border: 6px solid var(--white);
    box-shadow: 0 3px 10px rgba(0,0,0,0.3);
  }
  .dish-lamb { left: 58px; top: 650px; width: 200px; height: 200px;
    background: radial-gradient(circle at 45% 45%, #d9a070 0%, #9a5a30 55%, #5a3320 100%); }
  .dish-plate { left: 190px; top: 780px; width: 150px; height: 150px;
    background: radial-gradient(circle at 50% 50%, #f5efe6 0%, #e0d4c0 50%, #b79a70 100%); }
  .dish-steak { left: 40px; top: 830px; width: 200px; height: 200px;
    background: radial-gradient(circle at 50% 50%, #c6612a 0%, #7a3518 55%, #2a140c 100%); }

  .specialties { position: absolute; left: 430px; top: 730px; width: 440px; height: 64px; }
  .specialties-title { position: absolute; left: 40px; top: 6px; font-size: 34px; font-weight: 600; color: var(--white); }

  .menu { position: absolute; right: 50px; top: 812px; list-style: none; text-align: right; }
  .menu li { font-size: 20px; line-height: 30px; color: var(--ink); }
  .menu li::after {
    content: ""; display: inline-block; width: 10px; height: 10px; border-radius: 50%;
    background: var(--magenta); margin-left: 22px; vertical-align: middle;
  }

  .contact { position: absolute; left: 30px; color: var(--white); font-size: 23px; display: flex; align-items: flex-start; gap: 12px; }
  .contact-web { top: 1062px; }
  .contact-address { top: 1108px; line-height: 32px; }
  .contact svg { flex: none; margin-top: 4px; }

  .wifi { position: absolute; right: 40px; top: 1110px; display: flex; align-items: center; gap: 14px; color: var(--white); }
  .wifi-free { font-size: 40px; font-style: italic; font-weight: 600; }
</style>
</head>
<body>
<div class="flyer">
  <div class="venue-photo" role="img" aria-label="Night view of the restaurant terrace with its illuminated sign, tables and purple lighting"></div>

  <svg class="backdrop" width="870" height="1200" viewBox="0 0 870 1200" aria-hidden="true">
    <path d="M0 0 H870 V160 C650 230 300 150 0 205 Z" fill="var(--magenta)"/>
    <path d="M0 205 C300 150 650 230 870 160 V176 C650 250 300 170 0 222 Z" fill="var(--white)"/>
    <path d="M0 222 C300 170 650 250 870 176 V188 C650 262 300 182 0 232 Z" fill="var(--teal)"/>
    <path d="M0 690 C250 760 600 650 870 720 V1200 H0 Z" fill="var(--white)"/>
    <path d="M0 690 C250 760 600 650 870 720 V732 C600 664 250 774 0 704 Z" fill="var(--teal)"/>
    <path d="M430 736 C470 724 520 722 560 730 H870 V800 H430 Z" fill="var(--teal)"/>
    <path d="M445 728 C490 718 530 718 570 724 H870 V792 H445 Z" fill="var(--magenta)"/>
    <path d="M0 1030 C300 990 600 1060 870 1010 V1200 H0 Z" fill="var(--teal)"/>
    <path d="M0 1044 C300 1004 600 1074 870 1024 V1200 H0 Z" fill="var(--magenta)"/>
    <path d="M380 1200 C520 1140 700 1130 870 1150 V1200 Z" fill="var(--magenta-deep)" opacity="0.5"/>
  </svg>

  <div class="reservation">
    <p class="reservation-label">For Reservation</p>
    <p class="reservation-phone">922 40 18 53</p>
  </div>

  <div class="brand">
    <span class="brand-name">Paper Kite</span>
    <span class="brand-sub">Restaurant</span>
  </div>

  <div class="dish dish-lamb" role="img" aria-label="Grilled rack of lamb"></div>
  <div class="dish dish-steak" role="img" aria-label="Steak on the grill"></div>
  <div class="dish dish-plate" role="img" aria-label="Plated fish dish"></div>

  <div class="specialties"><h2 class="specialties-title">Our Specialties</h2></div>

  <ul class="menu">
    <li>Lorem ipsum dolor</li>
    <li>sit amet, consectetuer</li>
    <li>adipiscing elit</li>
    <li>Aenean commodo</li>
    <li>ligula eget dolor</li>
    <li>Aenean massaum socis</li>
  </ul>

  <p class="contact contact-web">
    <svg width="14" height="14" viewBox="0 0 14 14" aria-hidden="true"><circle cx="7" cy="7" r="5" fill="var(--white)"/></svg>
    <span>www.paperkite-restaurant.com</span>
  </p>
  <p class="contact contact-address">
    <svg width="18" height="26" viewBox="0 0 18 26" aria-hidden="true"><path d="M9 0C4 0 0 4 0 9c0 7 9 17 9 17s9-10 9-17c0-5-4-9-9-9z" fill="var(--white)"/><circle cx="9" cy="9" r="3.5" fill="var(--magenta)"/></svg>
    <span>Paseo del Mar, C.C Miramar, Playa Del Sol<br>Los Arenales</span>
  </p>

  <div class="wifi">
    <span class="wifi-free">free</span>
    <svg width="60" height="48" viewBox="0 0 60 48" aria-label="Wi-Fi">
      <path d="M4 18 A38 38 0 0 1 56 18" stroke="var(--white)" stroke-width="5" fill="none" stroke-linecap="round"/>
      <path d="M13 28 A24 24 0 0 1 47 28" stroke="var(--white)" stroke-width="5" fill="none" stroke-linecap="round"/>
      <path d="M22 37 A11 11 0 0 1 38 37" stroke="var(--white)" stroke-width="5" fill="none" stroke-linecap="round"/>
      <circle cx="30" cy="44" r="4" fill="var(--white)"/>
    </svg>
  </div>
</div>
</body>
</html>
```